Tri-fold flyer for Managed Services IT company

We need a tri-fold flyer design for our Managed Services IT company. Our website is here: https://harborlinetech.net. While we don't have to match our website we do want to incorporate the logo in the flyer. We would like a flyer that is *very* easy and quick to read/skim over and convey our message. Something like these:

https://www.pixelvendo.com/design/52837164

https://graphiqhub.com/postcard-flyer-design/contests/create-lead-generating-flyer-postcard-managed-services-company-861524

http://www.brimstackservices.com/managed-services-no-cost-one-month/

Target Market(s)

Business to business IT services

Industry/Entity Type

It Service

Font styles to use
Serif
Sans Serif

Requirements
Must have
• *very* easy and quick to read/skim over and convey our message
Should not have
• verbose, lots of text

```html
<!DOCTYPE html>
<html lang="en">
<head>
<meta charset="utf-8">
<title>Our Services – Tri-fold Flyer Panel</title>
<link rel="stylesheet" href="https://fonts.googleapis.com/css2?family=Bebas+Neue&family=Roboto+Condensed:wght@700&family=Open+Sans:wght@400;600&display=swap">
<style>
  :root {
    --sky-deep: #1479c2;
    --sky-light: #3fb2e8;
    --panel-dark: #1d1d1e;
    --hex-blue: #2aa0db;
    --text-white: #ffffff;
    --text-soft: #e9eef2;
    --cloud-deep: #1666b8;
    --cloud-light: #3aa9e4;
  }
  * { box-sizing: border-box; margin: 0; padding: 0; }
  html, body { width: 820px; height: 1200px; overflow: hidden; background: var(--panel-dark); }
  .flyer-panel {
    width: 820px; height: 1200px;
    display: flex; flex-direction: column;
    background: var(--panel-dark);
  }
  .services-header {
    height: 150px;
    background: linear-gradient(180deg, var(--sky-deep) 0%, var(--sky-light) 100%);
    display: flex; align-items: center; justify-content: center;
    border-top: 6px solid #0d4f85;
  }
  .services-title {
    font-family: "Bebas Neue", "Oswald", sans-serif;
    font-weight: 400;
    font-size: 74px;
    letter-spacing: 1px;
    color: var(--text-white);
    line-height: 1;
    padding-top: 10px;
  }
  .services-grid {
    flex: 1;
    display: grid;
    grid-template-columns: repeat(3, 1fr);
    grid-template-rows: repeat(3, 1fr);
    padding: 40px 20px 10px;
  }
  .service-item {
    display: flex; flex-direction: column; align-items: center;
    text-align: center;
    padding: 0 22px;
  }
  .service-icon { width: 56px; height: 64px; margin-bottom: 22px; }
  .service-name {
    font-family: "Roboto Condensed", "Arial Narrow", sans-serif;
    font-weight: 700;
    font-size: 29px;
    color: var(--text-white);
    margin-bottom: 18px;
  }
  .service-text {
    font-family: "Open Sans", Arial, sans-serif;
    font-size: 18px;
    line-height: 1.35;
    color: var(--text-soft);
  }
  .cloud-footer {
    height: 100px;
    background: linear-gradient(180deg, var(--cloud-deep) 0%, var(--cloud-light) 100%);
  }
</style>
</head>
<body>
<main class="flyer-panel">
  <header class="services-header">
    <h1 class="services-title">Our Services</h1>
  </header>

  <section class="services-grid">
    <article class="service-item">
      <svg class="service-icon" viewBox="0 0 52 60" aria-hidden="true">
        <polygon points="26,0 52,15 52,45 26,60 0,45 0,15" fill="var(--hex-blue)"/>
        <path d="M36 30a10 10 0 1 1-4-8" fill="none" stroke="#fff" stroke-width="2.2"/>
        <path d="M33 19l0 5 5 0" fill="none" stroke="#fff" stroke-width="2"/>
        <text x="26" y="33" font-family="Open Sans, sans-serif" font-size="6.5" font-weight="600" fill="#fff" text-anchor="middle">24/7</text>
        <circle cx="36" cy="37" r="4" fill="#fff"/>
      </svg>
      <h2 class="service-name">Managed IT</h2>
      <p class="service-text">Strategically optimize and protect your infrastructure with 24/7/365 Proactive Monitoring.</p>
    </article>

    <article class="service-item">
      <svg class="service-icon" viewBox="0 0 52 60" aria-hidden="true">
        <polygon points="26,0 52,15 52,45 26,60 0,45 0,15" fill="var(--hex-blue)"/>
        <circle cx="23" cy="28" r="7" fill="none" stroke="#fff" stroke-width="4" stroke-dasharray="3 2.5"/>
        <circle cx="23" cy="28" r="3" fill="#fff"/>
        <circle cx="33" cy="37" r="4" fill="none" stroke="#fff" stroke-width="3" stroke-dasharray="2 1.6"/>
      </svg>
      <h2 class="service-name">Industry Specific</h2>
      <p class="service-text">Looking for IT Solutions specific to your Industry?</p>
    </article>

    <article class="service-item">
      <svg class="service-icon" viewBox="0 0 52 60" aria-hidden="true">
        <polygon points="26,0 52,15 52,45 26,60 0,45 0,15" fill="var(--hex-blue)"/>
        <path d="M19 18h10l5 5v19H19z" fill="#fff"/>
        <circle cx="26" cy="34" r="5" fill="var(--hex-blue)"/>
        <circle cx="26" cy="34" r="1.6" fill="#fff"/>
      </svg>
      <h2 class="service-name">Software Services</h2>
      <p class="service-text">Have every team member collaborate together on the same project from any location!</p>
    </article>

    <article class="service-item">
      <svg class="service-icon" viewBox="0 0 52 60" aria-hidden="true">
        <polygon points="26,0 52,15 52,45 26,60 0,45 0,15" fill="var(--hex-blue)"/>
        <path d="M26 16l11 4v9c0 7-5 12-11 15-6-3-11-8-11-15v-9z" fill="none" stroke="#fff" stroke-width="2.2"/>
        <path d="M26 20l8 3v6c0 5-4 9-8 11z" fill="#fff"/>
      </svg>
      <h2 class="service-name">Security Services</h2>
      <p class="service-text">Advanced security systems help protect your data and keep your business up and running.</p>
    </article>

    <article class="service-item">
      <svg class="service-icon" viewBox="0 0 52 60" aria-hidden="true">
        <polygon points="26,0 52,15 52,45 26,60 0,45 0,15" fill="var(--hex-blue)"/>
        <g fill="none" stroke="#fff" stroke-width="2.2">
          <ellipse cx="26" cy="20" rx="10" ry="3.5"/>
          <path d="M16 20v20c0 2 4.5 3.5 10 3.5s10-1.5 10-3.5V20"/>
          <path d="M16 27c0 2 4.5 3.5 10 3.5s10-1.5 10-3.5"/>
          <path d="M16 34c0 2 4.5 3.5 10 3.5s10-1.5 10-3.5"/>
        </g>
      </svg>
      <h2 class="service-name">IT Data Services</h2>
      <p class="service-text">Is your data secure? Would it survive a disaster? Can you afford to take a chance?</p>
    </article>

    <article class="service-item">
      <svg class="service-icon" viewBox="0 0 52 60" aria-hidden="true">
        <polygon points="26,0 52,15 52,45 26,60 0,45 0,15" fill="var(--hex-blue)"/>
        <rect x="15" y="23" width="22" height="16" rx="1.5" fill="#fff"/>
        <rect x="21" y="19" width="10" height="5" fill="none" stroke="#fff" stroke-width="2"/>
        <rect x="15" y="29" width="22" height="1.6" fill="var(--hex-blue)"/>
      </svg>
      <h2 class="service-name">Business Services</h2>
      <p class="service-text">Empower your business to go far beyond the restraints of a typical phone system solution.</p>
    </article>

    <article class="service-item">
      <svg class="service-icon" viewBox="0 0 52 60" aria-hidden="true">
        <polygon points="26,0 52,15 52,45 26,60 0,45 0,15" fill="var(--hex-blue)"/>
        <path d="M17 38a6 6 0 0 1 1-12 8 8 0 0 1 15-2 7 7 0 0 1 2 14z" fill="#fff"/>
      </svg>
      <h2 class="service-name">Cloud IT</h2>
      <p class="service-text">Cloud IT is the future of small and medium business technology management.</p>
    </article>

    <article class="service-item">
      <svg class="service-icon" viewBox="0 0 52 60" aria-hidden="true">
        <polygon points="26,0 52,15 52,45 26,60 0,45 0,15" fill="var(--hex-blue)"/>
        <rect x="18" y="22" width="16" height="16" fill="none" stroke="#fff" stroke-width="2.2"/>
        <rect x="22" y="26" width="8" height="8" fill="#fff"/>
        <g stroke="#fff" stroke-width="1.6">
          <path d="M22 22v-4M26 22v-4M30 22v-4M22 38v4M26 38v4M30 38v4M18 26h-4M18 30h-4M18 34h-4M34 26h4M34 30h4M34 34h4"/>
        </g>
      </svg>
      <h2 class="service-name">Hardware Services</h2>
      <p class="service-text">Can your enterprise afford to replace the essential hardware for your company?</p>
    </article>

    <article class="service-item">
      <svg class="service-icon" viewBox="0 0 52 60" aria-hidden="true">
        <polygon points="26,0 52,15 52,45 26,60 0,45 0,15" fill="var(--hex-blue)"/>
        <g fill="none" stroke="#fff" stroke-width="2.6" stroke-linecap="round">
          <path d="M14 27a17 17 0 0 1 24 0"/>
          <path d="M18 31a11 11 0 0 1 16 0"/>
          <path d="M22 35a5 5 0 0 1 8 0"/>
        </g>
        <circle cx="26" cy="39" r="2" fill="#fff"/>
      </svg>
      <h2 class="service-name">Media &amp; Internet</h2>
      <p class="service-text">Improving your company's presence on the internet is essential.</p>
    </article>
  </section>

  <footer class="cloud-footer" role="img" aria-label="Band of soft blue clouds along the bottom edge"></footer>
</main>
</body>
</html>
```